Property Management Company Business Cards

Need business cards for a property management company located in Michigan. We manage houses for clients all over the world. Young and modern company, looking for eye catching design. Please work with the attached logo.

Industry/Entity Type

Property Management

Requirements
Must have
• Need lines for address, telephone number, fax number, web site.

Also lines for name, and job title

```html
<!DOCTYPE html>
<html lang="en">
<head>
<meta charset="utf-8">
<title>Northfield Global Management – Folder and Business Card</title>
<link href="https://fonts.googleapis.com/css2?family=Open+Sans:wght@400;600;700&display=swap" rel="stylesheet">
<style>
  :root {
    --brand-blue: #29a9e1;
    --brand-blue-deep: #1e98d3;
    --paper: #f7f8f8;
    --ink: #2d2f33;
    --ink-soft: #55585d;
    --stage-top: #8f9194;
    --stage-bottom: #e6e7e8;
  }
  * { margin: 0; padding: 0; box-sizing: border-box; }
  html, body { width: 1200px; height: 861px; overflow: hidden; }
  body {
    font-family: "Open Sans", Arial, sans-serif;
    background: linear-gradient(180deg, var(--stage-top) 0%, var(--stage-bottom) 70%, #f1f1f1 100%);
    position: relative;
  }

  /* ---------- Folder spread ---------- */
  .folder {
    position: absolute;
    left: 60px;
    top: 150px;
    width: 700px;
    height: 470px;
    box-shadow: 0 18px 30px rgba(0,0,0,0.25);
  }
  .folder svg { position: absolute; inset: 0; }
  .folder-brand {
    position: absolute;
    left: 418px;
    top: 386px;
    display: flex;
    align-items: center;
    gap: 10px;
  }
  .brand-dot {
    width: 22px; height: 22px;
    border-radius: 50%;
    background: var(--ink);
    flex: none;
  }
  .brand-name {
    font-weight: 700;
    font-size: 17px;
    letter-spacing: 0.5px;
    text-transform: uppercase;
    color: var(--ink);
    line-height: 1;
  }
  .folder-footer {
    position: absolute;
    left: 22px;
    bottom: 22px;
    color: var(--ink-soft);
  }
  .folder-footer .brand-name { font-size: 9px; }
  .folder-footer .brand-dot { width: 11px; height: 11px; }
  .folder-footer .brand-row { display: flex; align-items: center; gap: 5px; margin-bottom: 4px; }
  .folder-footer p { font-size: 5.5px; line-height: 1.5; }

  /* ---------- Business card ---------- */
  .card {
    position: absolute;
    left: 820px;
    top: 470px;
    width: 340px;
    height: 200px;
    background: var(--paper);
    box-shadow: 0 12px 22px rgba(0,0,0,0.22);
    overflow: hidden;
  }
  .card svg { position: absolute; inset: 0; }
  .card-brand {
    position: absolute;
    left: 16px;
    top: 28px;
    display: flex;
    align-items: center;
    gap: 8px;
  }
  .card-brand .brand-dot { background: #ffffff; width: 18px; height: 18px; }
  .card-brand .brand-name { color: #ffffff; font-size: 13.5px; }
  .card-person {
    position: absolute;
    left: 20px;
    top: 118px;
  }
  .person-name {
    font-weight: 700;
    font-size: 15px;
    color: var(--brand-blue-deep);
    line-height: 1.1;
  }
  .person-title {
    font-weight: 600;
    font-size: 9px;
    color: var(--ink);
  }
  .card-contact {
    position: absolute;
    left: 168px;
    top: 124px;
    list-style: none;
    font-size: 7.5px;
    color: var(--ink);
  }
  .card-contact li {
    display: flex;
    align-items: flex-start;
    gap: 5px;
    margin-bottom: 6px;
    line-height: 1.35;
  }
  .card-contact svg { position: static; width: 8px; height: 8px; flex: none; margin-top: 1px; }
</style>
</head>
<body>

  <section class="folder" aria-label="Presentation folder, outside spread">
    <svg viewBox="0 0 700 470" width="700" height="470">
      <rect width="700" height="470" fill="var(--brand-blue)"/>
      <path d="M0 355 L300 355 C420 352 560 300 700 245 L700 470 L0 470 Z" fill="var(--paper)"/>
      <path d="M250 322 C380 305 500 278 620 228 C500 262 380 292 250 322 Z" fill="#ffffff"/>
      <line x1="350" y1="0" x2="350" y2="470" stroke="#1b7fb0" stroke-opacity="0.35" stroke-width="2"/>
    </svg>

    <div class="folder-brand">
      <span class="brand-dot"></span>
      <span class="brand-name">Northfield Global Management</span>
    </div>

    <div class="folder-footer">
      <div class="brand-row">
        <span class="brand-dot"></span>
        <span class="brand-name">Northfield Global Management</span>
      </div>
      <p>15th Floor, Lorem Ipsum Avenue, Dolor Sit Amet City</p>
      <p>Telephone: 123.456.7890 • Fax: 098.765.4321</p>
      <p>E-mail: hello@northfieldmgmt.com • Web: www.northfieldmgmt.com</p>
    </div>
  </section>

  <section class="card" aria-label="Business card, front">
    <svg viewBox="0 0 340 200" width="340" height="200">
      <path d="M0 0 H340 V78 C250 82 150 94 0 102 Z" fill="var(--brand-blue)"/>
      <path d="M70 106 C150 100 230 92 310 80 C230 96 150 104 70 106 Z" fill="var(--brand-blue)"/>
      <path d="M60 102 C150 96 240 88 330 76 C250 86 150 94 60 102 Z" fill="#ffffff"/>
    </svg>

    <div class="card-brand">
      <span class="brand-dot"></span>
      <span class="brand-name">Northfield Global Management</span>
    </div>

    <div class="card-person">
      <p class="person-name">Name Surname</p>
      <p class="person-title">Your Position</p>
    </div>

    <ul class="card-contact">
      <li>
        <svg viewBox="0 0 10 10" aria-hidden="true"><path d="M5 0.5 L9.5 5 H8 V9.5 H2 V5 H0.5 Z" fill="var(--brand-blue)"/></svg>
        <span>15th floor, Lorem Ipsum Avenue,<br>Dolor Sit Amet City</span>
      </li>
      <li>
        <svg viewBox="0 0 10 10" aria-hidden="true"><path d="M2 0.5 L4 2.5 L3 4 C3.8 5.6 4.6 6.4 6 7 L7.5 6 L9.5 8 L8 9.5 C4 9 1 6 0.5 2 Z" fill="var(--brand-blue)"/></svg>
        <span>123.456.7890</span>
      </li>
      <li>
        <svg viewBox="0 0 10 10" aria-hidden="true"><rect x="2.5" y="0.5" width="5" height="3" fill="var(--brand-blue)"/><rect x="0.5" y="4" width="9" height="5" rx="1" fill="var(--brand-blue)"/></svg>
        <span>098.765.4321</span>
      </li>
      <li>
        <svg viewBox="0 0 10 10" aria-hidden="true"><rect x="0.5" y="1" width="9" height="8" rx="1" fill="none" stroke="var(--brand-blue)" stroke-width="1.2"/><line x1="0.5" y1="3.5" x2="9.5" y2="3.5" stroke="var(--brand-blue)" stroke-width="1.2"/></svg>
        <span>www.northfieldmgmt.com</span>
      </li>
    </ul>
  </section>

</body>
</html>
```